Wellness Coach needs a Business Card

I need a business card for a start-up coaching business called Brightfern Vitality Partners. I don't have a logo as such but I am looking to have a web page created in a few months time and hopefully the person who designs this card will be able to do or help with the web project. This business card will be used primarily for networking and for initial clients.

As the name implies, the coaching focus is wide-ranging and includes multiple facets of health and wellness, including physical, mental, spiritual, etc. I am a Personal Trainer so the main focus will be physical training, but with the other areas of life / wellness included.

My information for the card:

Rowan Tesdale
Director
Brightfern Vitality Partners

Phone: 0413 862051
Address: PO Box 615 Mitchell ACT 2911
email: rowan@brightfernvitalitypartners.com.au
web: http://www.brightfernvitalitypartners.com.au

Target Market(s)

People wanting to change their life by getting fit and by addressing issues in their lives that are holding them back. I will target people already into fitness but who want to extend their approach into life coaching.

Industry/Entity Type

Health

Requirements
Must have
• - I am keen on a single sided business card design but if your design lends itself to a double sided design then I'm open to that thanks.

- I love the idea of fresh - something that represents the awakening of somebody who has been dormant. Lime green strikes me as fresh, but this is just an idea, not mandatory.
Nice to have
• - I'm keen for minimisation but I don't mind an image in the background taking up the whole space, as long as it is not too busy.

- Two types of images that I can visualise are a mountain summit or a path leading into nature or up a mountain - an adventure! Again, not mandatory, just an idea.
Should not have
• - I'm not keen on over-crowding.
- One image I'm not keen on is someone standing on top of a mountain with their arms in the air - too cliché.

```html
<!DOCTYPE html>
<html lang="en">
<head>
<meta charset="utf-8">
<title>Brightfern Vitality Partners – Business Card</title>
<link href="https://fonts.googleapis.com/css2?family=Cinzel:wght@400;600;700&family=Open+Sans:wght@400;700&display=swap" rel="stylesheet">
<style>
  :root {
    --lime: #84c92a;
    --lime-light: #a6d94f;
    --lime-deep: #6fb81d;
    --ink: #1c1a17;
    --ink-soft: #3a3632;
    --paper: #ffffff;
    --backdrop: #c4c4c4;
  }
  * { margin: 0; padding: 0; box-sizing: border-box; }
  html, body { width: 1200px; height: 900px; overflow: hidden; }
  body {
    position: relative;
    background: var(--backdrop);
    font-family: "Open Sans", Arial, sans-serif;
  }
  .card {
    position: absolute;
    width: 620px;
    height: 354px;
    overflow: hidden;
  }

  /* Front side */
  .card-front {
    left: 200px;
    top: 70px;
    background: linear-gradient(100deg, var(--lime-deep) 0%, var(--lime) 45%, var(--lime-light) 100%);
    display: flex;
    align-items: center;
    justify-content: center;
  }
  .card-front .brand-name {
    font-family: "Cinzel", "Times New Roman", serif;
    font-weight: 400;
    font-size: 30px;
    letter-spacing: 1px;
    color: var(--paper);
  }

  /* Back side */
  .card-back {
    left: 380px;
    top: 470px;
    background: var(--paper);
  }
  .logo-block {
    position: absolute;
    top: 34px;
    left: 0;
    right: 0;
    display: flex;
    align-items: center;
    justify-content: center;
    gap: 14px;
  }
  .logo-mark {
    width: 26px;
    height: 26px;
    border-radius: 50%;
    background: var(--lime);
  }
  .logo-name {
    font-family: "Cinzel", "Times New Roman", serif;
    font-weight: 700;
    font-size: 26px;
    color: var(--ink);
  }
  .info-band {
    position: absolute;
    top: 96px;
    left: 0;
    right: 0;
    height: 206px;
    background: var(--lime);
    border-top: 3px solid var(--lime);
  }
  .info-band::before,
  .info-band::after {
    content: "";
    position: absolute;
    left: 0;
    right: 0;
    height: 3px;
    background: var(--paper);
  }
  .info-band::before { top: 0; }
  .info-band::after { top: 9px; }
  .person {
    text-align: center;
    margin-top: 24px;
  }
  .person-name {
    font-family: "Cinzel", "Times New Roman", serif;
    font-weight: 700;
    font-size: 24px;
    color: var(--ink);
    line-height: 1.1;
  }
  .person-title {
    font-family: "Cinzel", "Times New Roman", serif;
    font-size: 16px;
    color: var(--ink-soft);
    line-height: 1.1;
  }
  .contact-list {
    list-style: none;
    text-align: center;
    margin-top: 16px;
    font-size: 15px;
    line-height: 1.45;
    color: var(--ink);
  }
  .contact-list b { font-weight: 700; }
  .website {
    position: absolute;
    bottom: 14px;
    left: 0;
    right: 0;
    text-align: center;
    font-size: 16px;
    letter-spacing: 1.5px;
    color: var(--ink-soft);
  }
</style>
</head>
<body>
  <section class="card card-front" aria-label="Business card front">
    <p class="brand-name">Brightfern Vitality Partners</p>
  </section>

  <section class="card card-back" aria-label="Business card back">
    <div class="logo-block">
      <span class="logo-mark" aria-hidden="true"></span>
      <span class="logo-name">Brightfern Vitality Partners</span>
    </div>
    <div class="info-band">
      <div class="person">
        <p class="person-name">Rowan Tesdale</p>
        <p class="person-title">Director</p>
      </div>
      <ul class="contact-list">
        <li><b>M:</b> 0413 862051</li>
        <li><b>E:</b> rowan@brightfernvitalitypartners.com.au</li>
        <li>PO Box 615 Larkspur Vale 2950</li>
      </ul>
    </div>
    <p class="website">www.brightfernvitalitypartners.com.au</p>
  </section>
</body>
</html>
```